Packaging designed for both the bar and the box for retail and online sales

The name of the product is Plume Crumb. We manufacture a consumer package good product that's a healthy edible cookie dough bar. The product look, feels and tastes like cookie dough. It's sold in the refrigerator section of retail stores next to cookie dough and tundra loaf. The product is Gluten Free, Diary Free and include B-12, Biotin and Collagen. The ingredients are natural. When design this think about who eat cookie dough and how to engage the buyer in purchasing the product.

We needs design packaging designed for both the bar and the box. I have attached the die lines for both products.

Target Market(s)

Our customer is 16-45. Primarily female but really anyone. Middle to upper income. Interest include healthy life style and yoga. Like to eat something sweet but not feel guilty.

Colors

Designer to choose colors to be used in the design.

Requirements
Must have
• Must be clean, warm, inviting. Brand designs I really like are Tundra Loaf.
Should not have
• Should not have a photo of food

```html
<!DOCTYPE html>
<html lang="en">
<head>
<meta charset="utf-8">
<title>Plume Crumb – Box and Bar Packaging</title>
<link rel="stylesheet" href="https://fonts.googleapis.com/css2?family=Oswald:wght@500;600&display=swap">
<style>
  :root {
    --cocoa: #2a150f;
    --ember: #e0520f;
    --ember-dark: #c9450b;
    --paper: #f4f4f6;
    --strip: #e6e5e8;
    --ink: #241310;
    --stage: #f6f1ec;
    --cookie-light: #d08a3c;
    --cookie-dark: #9a5a22;
    --white: #ffffff;
  }
  * { box-sizing: border-box; margin: 0; padding: 0; }
  html, body { width: 1200px; height: 1200px; overflow: hidden; }
  body {
    position: relative;
    background: var(--stage);
    font-family: "Oswald", "Arial Narrow", sans-serif;
    font-weight: 500;
  }
  .artwork { position: absolute; left: 0; top: 0; width: 1200px; height: 1200px; }

  .label { position: absolute; line-height: 1; white-space: nowrap; }
  .brand-name { font-weight: 600; color: var(--ember); letter-spacing: -0.005em; }
  .claim { color: var(--white); }
  .claim.spaced { letter-spacing: 0.3em; }
  .nutrients {
    display: flex; align-items: center;
    color: var(--white); letter-spacing: -0.01em;
  }
  .nutrients .sep { display: block; width: 1.5px; height: 1.1em; background: rgba(255,255,255,0.85); }
  .net-weight { color: var(--ink); letter-spacing: 0.12em; }

  /* box front */
  .box-name { font-size: 104px; }
  .box-claim { font-size: 40px; }
  .box-nutrients { font-size: 30px; gap: 8px; }
  .box-net { font-size: 21px; }

  /* bar wrapper */
  .bar-name { font-size: 64px; }
  .bar-claim { font-size: 32px; }
  .bar-nutrients { font-size: 23px; gap: 6px; }
  .bar-net { font-size: 24px; }
</style>
</head>
<body>

  <svg class="artwork" viewBox="0 0 1200 1200" aria-hidden="true">
    <defs>
      <radialGradient id="dough" cx="45%" cy="40%" r="65%">
        <stop offset="0" stop-color="var(--cookie-light)"/>
        <stop offset="1" stop-color="var(--cookie-dark)"/>
      </radialGradient>
      <clipPath id="boxClip"><rect x="92" y="104" width="524" height="756"/></clipPath>
      <pattern id="crimpTop" x="770" y="292" width="10" height="10" patternUnits="userSpaceOnUse">
        <path d="M0 10 L5 2 L10 10 Z" fill="var(--cocoa)"/>
      </pattern>
      <pattern id="crimpBottom" x="770" y="1114" width="10" height="10" patternUnits="userSpaceOnUse">
        <path d="M0 0 L5 8 L10 0 Z" fill="var(--ember-dark)"/>
      </pattern>
    </defs>

    <!-- box front -->
    <g class="box-panel" clip-path="url(#boxClip)">
      <rect x="92" y="104" width="524" height="756" fill="var(--cocoa)"/>
      <g role="img" aria-label="Illustration of three chocolate chip cookie dough rounds">
        <circle cx="184" cy="612" r="70" fill="url(#dough)"/>
        <circle cx="528" cy="606" r="70" fill="url(#dough)"/>
        <circle cx="358" cy="552" r="120" fill="url(#dough)"/>
      </g>
      <path d="M92 648 Q340 604 616 652 L616 796 L92 796 Z" fill="var(--ember-dark)"/>
      <line x1="358" y1="660" x2="358" y2="730" stroke="var(--white)" stroke-width="2" opacity="0.85"/>
      <rect x="92" y="796" width="524" height="50" fill="var(--strip)"/>
      <rect x="92" y="846" width="524" height="14" fill="var(--ember-dark)"/>
    </g>

    <!-- bar wrapper -->
    <g class="bar-panel">
      <rect x="770" y="292" width="386" height="10" fill="url(#crimpTop)"/>
      <path d="M770 301 L1156 301 L1156 345 Q1138 390 1130 464 L786 464 Q778 390 770 345 Z" fill="var(--cocoa)"/>
      <rect x="786" y="464" width="344" height="420" fill="var(--paper)"/>
      <circle cx="952" cy="772" r="104" fill="url(#dough)" role="img" aria-label="Illustration of a chocolate chip cookie dough round"/>
      <path d="M786 870 Q950 850 1130 874 L1132 1010 L784 1010 Z" fill="var(--ember)"/>
      <line x1="962" y1="892" x2="962" y2="948" stroke="var(--white)" stroke-width="1.5" opacity="0.85"/>
      <path d="M784 1010 L1132 1010 L1138 1056 L778 1056 Z" fill="var(--strip)"/>
      <path d="M778 1056 L1138 1056 L1156 1070 L1156 1115 L770 1115 L770 1070 Z" fill="var(--ember-dark)"/>
      <rect x="770" y="1114" width="386" height="10" fill="url(#crimpBottom)"/>
    </g>
  </svg>

  <!-- box front text -->
  <section aria-label="Plume Crumb box front">
    <div class="label brand-name box-name" style="left:146px; top:165px;">Plume</div>
    <div class="label brand-name box-name" style="left:276px; top:269px;">Crumb</div>

    <div class="label claim box-claim" style="left:210px; top:652px;">GLUTEN</div>
    <div class="label claim box-claim spaced" style="left:210px; top:690px;">FREE</div>
    <div class="label claim box-claim" style="left:398px; top:652px;">DIARY</div>
    <div class="label claim box-claim" style="left:398px; top:690px;">FREE</div>

    <div class="label nutrients box-nutrients" style="left:210px; top:748px;">
      <span>COLLAGEN</span><i class="sep"></i><span>BIOTIN</span><i class="sep"></i><span>B-12</span>
    </div>

    <div class="label net-weight box-net" style="left:92px; width:524px; text-align:center; top:811px;">NET WT.23 OZ(5G)</div>
  </section>

  <!-- bar wrapper text -->
  <section aria-label="Plume Crumb bar wrapper">
    <div class="label brand-name bar-name" style="left:836px; top:503px;">Plume</div>
    <div class="label brand-name bar-name" style="left:884px; top:567px;">Crumb</div>

    <div class="label claim bar-claim" style="left:845px; top:886px;">GLUTEN</div>
    <div class="label claim bar-claim spaced" style="left:845px; top:918px;">FREE</div>
    <div class="label claim bar-claim" style="left:994px; top:886px;">DIARY</div>
    <div class="label claim bar-claim" style="left:994px; top:918px;">FREE</div>

    <div class="label nutrients bar-nutrients" style="left:845px; top:966px;">
      <span>COLLAGEN</span><i class="sep"></i><span>BIOTIN</span><i class="sep"></i><span>B-12</span>
    </div>

    <div class="label net-weight bar-net" style="left:784px; width:348px; text-align:center; top:1021px;">NET WT.23 OZ(5G)</div>
  </section>

</body>
</html>
```